R7M Meridian Business Card Design

We need a business card created for our New Business "R7M Meridian"<br/><br/>The business card design is up to you however the following information must be on the business card:<br/><br/>Front of the business card -<br/>Email :dorianv@r7mmeridian.nz<br/>Mobile: +64 (0) 22 4871 659<br/>Website: www.r7mmeridian.nz<br/>Card Owner Name: Dorian Valcourt<br/>Company Title: Business Development Manager<br/>Slogan: "The BEST of both worlds". <br/>Logo On the front attached to the design brief<br/><br/>On the back: <br/>Space on the back for 4 more versions of the logo across the bottom of the card indicating different subsidiary brands - R7M Coffee, R7M Arts, R7M ?? (The card will be used for all of these brands - We Will add the extra subsidiary logos to the design once the design is finished (We are a graphics design team). <br/><br/>Other than that we want a premium feeling logo that remains universally usable depending on the business entity that we are using the card for. The use of bright bold colours would be great but we still want the card to feel premium.
Target Market(s)
Gift Design and Manufacturing Companies
Contact Information for Business Card
Front of the business card -
Email :dorianv@r7mmeridian.nz
Mobile: +64 (0) 22 4871 659
Website: www.r7mmeridian.nz
Card Owner Name: Dorian Valcourt
Company Title: Business Development Manager
Slogan: "The BEST of both worlds".
Logo On the front attached to the design brief

```html
<!DOCTYPE html>
<html lang="en">
<head>
<meta charset="utf-8">
<title>R7M Meridian Business Card</title>
<link rel="stylesheet" href="https://fonts.googleapis.com/css2?family=Roboto:wght@400;500&display=swap">
<style>
  :root {
    --backdrop: #a3a3a3;
    --card: #1f1f1f;
    --accent: #3a46b4;
    --text: #a9a9a9;
    --text-soft: #9a9a9a;
  }
  * { margin: 0; padding: 0; box-sizing: border-box; }
  html, body {
    width: 1200px;
    height: 1055px;
    overflow: hidden;
    background: var(--backdrop);
    font-family: "Roboto", Arial, sans-serif;
  }
  .canvas { position: relative; width: 1200px; height: 1055px; }
  .card {
    position: absolute;
    top: 183px;
    width: 374px;
    height: 655px;
    background: var(--card);
  }
  .card--front { left: 181px; }
  .card--back { left: 647px; }
  .front-frame {
    position: absolute;
    inset: 10px;
    border: 1.5px solid var(--accent);
  }
  .line {
    position: absolute;
    left: 0;
    width: 100%;
    text-align: center;
    transform: translateY(-50%);
    color: var(--text);
  }
  .owner-name { top: 137px; font-size: 23px; font-weight: 500; letter-spacing: 0.8px; }
  .owner-title { top: 160px; font-size: 14px; color: var(--text-soft); }
  .contact-icon {
    position: absolute;
    left: 50%;
    width: 24px;
    height: 24px;
    margin-left: -12px;
    margin-top: -12px;
  }
  .icon-phone { top: 233px; }
  .icon-mail { top: 324px; }
  .icon-web { top: 404px; }
  .contact-text { font-size: 14.5px; }
  .contact-phone { top: 279px; }
  .contact-mail { top: 362px; }
  .contact-web { top: 444px; }
  .slogan { top: 518px; font-size: 18.5px; font-weight: 500; letter-spacing: 1.6px; }
  .brand-lockup {
    position: absolute;
    top: 50%;
    left: 50%;
    transform: translate(-50%, -50%);
    display: flex;
    align-items: center;
    gap: 14px;
    white-space: nowrap;
  }
  .brand-dot {
    width: 22px;
    height: 22px;
    border-radius: 50%;
    border: 4px solid var(--accent);
  }
  .brand-name {
    font-size: 34px;
    font-weight: 500;
    color: var(--accent);
    letter-spacing: 1px;
  }
</style>
</head>
<body>
<main class="canvas">
  <section class="card card--front" aria-label="Card front">
    <div class="front-frame"></div>
    <h1 class="line owner-name">DORIAN VALCOURT</h1>
    <p class="line owner-title">Business Development Manager</p>

    <svg class="contact-icon icon-phone" viewBox="0 0 24 24" aria-hidden="true">
      <circle cx="12" cy="12" r="11" fill="none" stroke="var(--text)" stroke-width="1"/>
      <rect x="8.5" y="5.5" width="7" height="13" rx="1.2" fill="none" stroke="var(--text)" stroke-width="1.2"/>
      <line x1="11" y1="16.3" x2="13" y2="16.3" stroke="var(--text)" stroke-width="1"/>
    </svg>
    <p class="line contact-text contact-phone">+64 (0) 22 4871 659</p>

    <svg class="contact-icon icon-mail" viewBox="0 0 24 24" aria-hidden="true">
      <circle cx="12" cy="12" r="11" fill="none" stroke="var(--text)" stroke-width="1"/>
      <rect x="6.5" y="8" width="11" height="8" fill="var(--text)"/>
      <polyline points="6.5,8 12,12.5 17.5,8" fill="none" stroke="var(--card)" stroke-width="1"/>
    </svg>
    <p class="line contact-text contact-mail">dorianv@r7mmeridian.nz</p>

    <svg class="contact-icon icon-web" viewBox="0 0 24 24" aria-hidden="true">
      <circle cx="12" cy="12" r="11" fill="none" stroke="var(--text)" stroke-width="1"/>
      <circle cx="12" cy="12" r="6" fill="var(--text)"/>
      <ellipse cx="12" cy="12" rx="2.6" ry="6" fill="none" stroke="var(--card)" stroke-width="0.9"/>
      <line x1="6" y1="12" x2="18" y2="12" stroke="var(--card)" stroke-width="0.9"/>
    </svg>
    <p class="line contact-text contact-web">www.r7mmeridian.nz</p>

    <p class="line slogan">The BEST of both worlds</p>
  </section>

  <section class="card card--back" aria-label="Card back">
    <div class="brand-lockup">
      <span class="brand-dot"></span>
      <span class="brand-name">R7M Meridian</span>
    </div>
  </section>
</main>
</body>
</html>
```